Dental Health Door hanger for contest to attract new patients

We are a group dental practice located in Burlington, Ontario, Canada. We are looking to bring in new patients and are targeting a new subdivision as well as established neighbourhoods around it.

The door hanger we require is for a contest are offering that will run for approx. 6 months to win a $1000.00 travel gift card. The individual must come in person to drop off the ballot and during that time they will get a tour of the practice and meet key people. There is no requirement for them to make an appointment but that is the ultimate goal.

I have included:
- a picture we typically use, however it is not required (female smiling)
- Our logo with "your city your dentists" below it. We want that tagline removed
- our other logo
- the excel version of the map created to our location
- the current one attempted on our own and is missing something - like the concept but not the total look/ feel

The final design should make the person want to come in and book an appointment with us and at the very least call to schedule something with a dentist.

Target Market(s)

New subdivision and surrounding area for new patients

Industry/Entity Type

Dental Clinic

Colors

Designer to choose colors to be used in the design.

Requirements
Must have
• Our address is 1846 Pemberly Road, Burlington, Ontario L7M 2K8. Our phone number is 905-482-7150. We are located on the 3rd floor of the Corvane Family Health Centre.
Nice to have
• We only need to have a logo, our address, a ballot of some sort on the door hanger and the details about the contest, the rest is up to you. We are moving towards the slogan "what makes you smile" at some point so this can be incorporated if it works with the overall design.
Should not have
• Fluorescent colours

```html
<!DOCTYPE html>
<html lang="en">
<head>
<meta charset="utf-8">
<title>Maplecrest Dental – Door Hanger</title>
<link rel="stylesheet" href="https://fonts.googleapis.com/css2?family=Josefin+Sans:wght@400&family=Open+Sans:wght@400;700;800&display=swap">
<style>
  :root {
    --brand-blue: #2f5fab;
    --panel-grey: #545454;
    --arc-grey: #4b4b4b;
    --prize-yellow: #fff200;
    --paper: #ffffff;
    --ink: #141414;
    --page: #ffffff;
  }
  * { margin: 0; padding: 0; box-sizing: border-box; }
  html, body { width: 1200px; height: 1200px; overflow: hidden; background: var(--page); }
  .door-hanger {
    position: absolute;
    left: 380px; top: 106px;
    width: 440px; height: 988px;
    font-family: "Open Sans", Arial, sans-serif;
  }
  .hanger-shapes { position: absolute; inset: 0; width: 440px; height: 988px; }
  .brand {
    position: absolute; left: 0; right: 0; top: 240px;
    display: flex; align-items: center; justify-content: center; gap: 18px;
  }
  .brand-name {
    font-family: "Josefin Sans", sans-serif;
    font-weight: 400;
    font-variant: small-caps;
    font-size: 34px;
    color: var(--ink);
    letter-spacing: 0.5px;
    line-height: 1;
    padding-top: 6px;
  }
  .brand-square { width: 40px; height: 40px; background: var(--brand-blue); }
  .contest {
    position: absolute; left: 0; right: 0; top: 624px; height: 197px;
    display: flex; flex-direction: column; align-items: center; justify-content: center;
    color: var(--paper); font-weight: 800; text-transform: uppercase; line-height: 1;
  }
  .contest-lead { font-size: 34px; letter-spacing: 0.5px; }
  .contest-prize { font-size: 76px; color: var(--prize-yellow); margin: 8px 0 4px; letter-spacing: -1px; }
  .contest-item { font-size: 35px; letter-spacing: 0.3px; }
  .phone {
    position: absolute; left: 40px; width: 358px; top: 858px; height: 54px;
    display: flex; align-items: center; justify-content: center; gap: 14px;
    color: var(--prize-yellow); font-weight: 800; font-size: 34px; letter-spacing: -0.3px;
  }
  .phone svg { width: 30px; height: 30px; }
  .address {
    position: absolute; left: 0; right: 0; top: 912px; height: 32px;
    display: flex; align-items: center; justify-content: center; gap: 6px;
    color: var(--brand-blue); font-weight: 700; font-size: 12.5px;
  }
  .address svg { width: 11px; height: 14px; }
  .website {
    position: absolute; left: 0; right: 0; top: 944px; height: 44px;
    display: flex; align-items: center; justify-content: center; gap: 10px;
    color: var(--paper); font-weight: 400; font-size: 20px;
  }
  .website svg { width: 16px; height: 16px; }
</style>
</head>
<body>
<main class="door-hanger">
  <svg class="hanger-shapes" viewBox="0 0 440 988" aria-hidden="false">
    <defs>
      <linearGradient id="photoTones" x1="0" y1="0" x2="1" y2="1">
        <stop offset="0" stop-color="#3a3431"/>
        <stop offset="0.45" stop-color="#8c6a5a"/>
        <stop offset="0.7" stop-color="#d9b8a6"/>
        <stop offset="1" stop-color="#2a2624"/>
      </linearGradient>
    </defs>
    <rect class="base-blue" width="440" height="988" fill="var(--brand-blue)"/>
    <path class="logo-band-edge" d="M0,203 Q220,143 440,203 L440,366 L0,366 Z" fill="var(--arc-grey)"/>
    <path class="logo-band" d="M0,210 Q220,150 440,210 L440,366 Q220,274 0,366 Z" fill="var(--paper)"/>
    <path class="photo-frame" d="M0,366 Q220,274 440,366 L440,554 Q220,680 0,554 Z" fill="var(--arc-grey)"/>
    <g role="img" aria-label="Photo of a smiling young woman in a knit winter hat">
      <path class="photo-area" d="M0,372 Q220,282 440,372 L440,546 Q220,666 0,546 Z" fill="url(#photoTones)"/>
    </g>
    <rect class="contest-panel" x="0" y="624" width="440" height="197" fill="var(--panel-grey)"/>
    <path class="phone-tab" d="M78,858 L362,858 L398,912 L40,912 Z" fill="var(--panel-grey)"/>
    <rect class="address-strip" x="0" y="912" width="440" height="32" fill="var(--paper)"/>
    <path class="web-strip" d="M16,944 L424,944 L440,970 L440,988 L0,988 L0,970 Z" fill="var(--panel-grey)"/>
    <circle class="hang-hole" cx="220" cy="122" r="66" fill="var(--paper)" stroke="#d6d6d6" stroke-width="3"/>
  </svg>

  <div class="brand">
    <span class="brand-name">Maplecrest Dental</span>
    <span class="brand-square"></span>
  </div>

  <section class="contest">
    <p class="contest-lead">Enter to win a</p>
    <p class="contest-prize">$1000</p>
    <p class="contest-item">Travel gift card</p>
  </section>

  <p class="phone">
    <svg viewBox="0 0 24 24" fill="#ffffff"><path d="M6.6 10.8a15.1 15.1 0 0 0 6.6 6.6l2.2-2.2a1 1 0 0 1 1-.25 11.4 11.4 0 0 0 3.6.57 1 1 0 0 1 1 1V20a1 1 0 0 1-1 1A17 17 0 0 1 3 4a1 1 0 0 1 1-1h3.5a1 1 0 0 1 1 1c0 1.25.2 2.45.57 3.57a1 1 0 0 1-.25 1z"/></svg>
    905-482-7150
  </p>

  <p class="address">
    <svg viewBox="0 0 12 16" fill="var(--brand-blue)"><path d="M6 0a6 6 0 0 0-6 6c0 4.5 6 10 6 10s6-5.5 6-10a6 6 0 0 0-6-6zm0 8.5A2.5 2.5 0 1 1 6 3.5a2.5 2.5 0 0 1 0 5z"/></svg>
    1846 Pemberly Road, Burlington, Ontario L7M 2K8
  </p>

  <p class="website">
    <svg viewBox="0 0 16 16" fill="none" stroke="#ffffff" stroke-width="1.2"><circle cx="8" cy="8" r="7"/><ellipse cx="8" cy="8" rx="3" ry="7"/><path d="M1 8h14M2 4.5h12M2 11.5h12"/></svg>
    www.maplecrestdental.ca
  </p>
</main>
</body>
</html>
```